Poster Design for kebab shop products

need a new poster for our new blazer tray special, sign will be inside of shopping centre at different location to shop will need to stand out and draw customers to the store, MUST contain shops logo & picture added, poster size will be 76cm x 101cm so will need to suit that size

MUST ALSO CONTAIN THE FOLLOWING
Blazer Tray / HSP
Lamb & Chips
Chicken & Chips
Beef & Chips
+ Can $15

Target Market(s)

new customers

Industry/Entity Type

Retail

Font styles to use
Sans Serif

Colors

Designer to choose colors to be used in the design.

Requirements
Must have
• company logo
• picture of blazr tray provided
• Blazer Tray / HSP
• Lamb & Chips
• Chicken & Chips
• Beef & Chips
• + Can $15

```html
<!DOCTYPE html>
<html lang="en">
<head>
<meta charset="utf-8">
<title>Grill Haven – Blazer Tray / HSP</title>
<link rel="stylesheet" href="https://fonts.googleapis.com/css2?family=Alegreya:ital,wght@0,400;0,600;0,800;1,600&display=swap">
<style>
  :root {
    --brand-red: #a32e2c;
    --ink: #454545;
    --paper: #ffffff;
    --edge: #ece9e6;
    --sun: #f2a23a;
    --fries: #f0c443;
    --meat: #8a4f2f;
  }
  * { margin: 0; padding: 0; box-sizing: border-box; }
  html, body { width: 903px; height: 1200px; overflow: hidden; background: var(--edge); }
  .poster {
    position: relative;
    width: 903px;
    height: 1200px;
    background: var(--paper);
    font-family: "Alegreya", Georgia, serif;
    color: var(--ink);
    overflow: hidden;
  }
  .top-band {
    position: absolute; left: 0; top: 4px; width: 100%; height: 19px;
    background: var(--brand-red);
  }
  .brand {
    position: absolute; left: 0; top: 70px; width: 100%;
    display: flex; justify-content: center; align-items: center; gap: 14px;
  }
  .brand-dot {
    width: 46px; height: 46px; border-radius: 50%; background: var(--sun);
  }
  .brand-name {
    font-weight: 800; font-size: 48px; color: var(--brand-red); line-height: 1;
  }
  .rule {
    position: absolute; left: 89px; top: 208px; width: 728px; height: 3px;
    background: var(--brand-red);
  }
  .headline {
    position: absolute; left: 0; top: 232px; width: 100%;
    text-align: center; font-weight: 800; line-height: 1;
    text-shadow: 0 2px 2px rgba(0,0,0,0.18);
  }
  .headline-top { display: block; font-size: 112px; letter-spacing: 10px; height: 118px; }
  .headline-bottom { display: block; font-size: 112px; letter-spacing: 6px; }
  .chevron { position: absolute; top: 254px; width: 64px; height: 66px; }
  .chevron-left { left: 89px; }
  .chevron-right { right: 86px; }
  .photo {
    position: absolute; left: 0; top: 470px; width: 100%; height: 655px;
    background:
      radial-gradient(ellipse 62% 34% at 50% 66%, rgba(138,79,47,0.95), rgba(138,79,47,0) 100%),
      linear-gradient(180deg, #ffffff 0%, #f7f4f0 22%, var(--fries) 42%, #e8b23a 100%);
  }
  .menu {
    position: absolute; left: 92px; top: 484px; width: 725px; height: 76px;
    font-size: 29px; letter-spacing: 2.5px; line-height: 44px;
  }
  .menu-col { position: absolute; top: 0; list-style: none; }
  .menu-col-left { left: 0; }
  .menu-col-right { left: 419px; }
  .menu-divider {
    position: absolute; left: 360px; top: 0; width: 1.5px; height: 74px; background: var(--ink);
  }
  .tags {
    position: absolute; left: 92px; top: 591px; width: 725px;
    display: flex; justify-content: space-between;
  }
  .tag {
    width: 196px; height: 45px; background: var(--brand-red); color: var(--paper);
    font-style: italic; font-weight: 600; font-size: 23px; letter-spacing: 2px;
    display: flex; align-items: center; justify-content: center;
  }
  .bottom-band {
    position: absolute; left: 0; top: 1125px; width: 100%; height: 55px;
    background: var(--brand-red); color: var(--paper);
    display: flex; align-items: center; justify-content: center;
    font-weight: 600; font-size: 13px; letter-spacing: 1.5px;
  }
  .bottom-edge {
    position: absolute; left: 0; top: 1180px; width: 100%; height: 20px; background: var(--edge);
  }
</style>
</head>
<body>
<main class="poster">
  <div class="top-band"></div>

  <header class="brand">
    <span class="brand-dot"></span>
    <span class="brand-name">Grill Haven</span>
  </header>

  <div class="rule"></div>

  <div class="photo" role="img" aria-label="Photo of a blazer tray: shaved kebab meat over chips with garlic and chilli sauce in a foam takeaway box"></div>

  <svg class="chevron chevron-left" viewBox="0 0 64 66" aria-hidden="true">
    <polyline points="4,4 30,33 4,62" fill="none" stroke="var(--brand-red)" stroke-width="10"/>
    <polyline points="30,4 56,33 30,62" fill="none" stroke="var(--brand-red)" stroke-width="10"/>
  </svg>
  <svg class="chevron chevron-right" viewBox="0 0 64 66" aria-hidden="true">
    <polyline points="60,4 34,33 60,62" fill="none" stroke="var(--brand-red)" stroke-width="10"/>
    <polyline points="34,4 8,33 34,62" fill="none" stroke="var(--brand-red)" stroke-width="10"/>
  </svg>

  <h1 class="headline">
    <span class="headline-top">BLAZER</span>
    <span class="headline-bottom">TRAY/HSP</span>
  </h1>

  <section class="menu">
    <ul class="menu-col menu-col-left">
      <li>- Lamb &amp; Chips</li>
      <li>- Chicken &amp; Chips</li>
    </ul>
    <div class="menu-divider"></div>
    <ul class="menu-col menu-col-right">
      <li>- Beef &amp; Chips</li>
      <li>- + Can $15</li>
    </ul>
  </section>

  <div class="tags">
    <span class="tag">HALAL</span>
    <span class="tag">SNACK</span>
    <span class="tag">PACK</span>
  </div>

  <footer class="bottom-band">BLAZER TRAY - HALAL SNACK PACK</footer>
  <div class="bottom-edge"></div>
</main>
</body>
</html>
```